GKRB-Postcard

We need a postcard design of a book. The card will be mailed out by Holbar Press to church leaders. Attached, please find a photo of the book cover, Word doc. with the message that should placed on the card, and a pre-designed sample. You may use a similar layout as the PDF sample or something more attractive. If you can, copy the publisher's logo and book information from the PDF file. Thank you.

Industry/Entity Type

Church

```html
<!DOCTYPE html>
<html lang="en">
<head>
<meta charset="utf-8">
<title>GKRB Postcard – The Enemy in Modern Eden</title>
<link rel="stylesheet" href="https://fonts.googleapis.com/css2?family=Questrial&family=Open+Sans:wght@400;700&family=EB+Garamond:wght@400;600&display=swap">
<style>
  :root {
    --stage: #e9e6e1;
    --cover-black: #0b0b0c;
    --skin-dark: #3a2a20;
    --skin-mid: #8a6a52;
    --globe-blue: #2d5b8c;
    --globe-deep: #0f2744;
    --title-red: #d42a2a;
    --title-white: #f2f2f2;
    --title-grey: #b9b9b9;
    --ink: #1d1d1d;
    --body-ink: #333333;
    --panel-light: #f1f1f1;
    --panel-mid: #d6d6d6;
    --card-white: #ffffff;
    --stamp-line: #b5b5b5;
  }
  * { box-sizing: border-box; margin: 0; padding: 0; }
  html, body { width: 1200px; height: 712px; overflow: hidden; }
  body { background: var(--stage); position: relative; font-family: "Open Sans", sans-serif; }

  /* Book cover */
  .book-cover {
    position: absolute; left: 30px; top: 64px; width: 460px; height: 592px;
    background: var(--cover-black); overflow: hidden;
    box-shadow: 0 6px 18px rgba(0,0,0,.35);
  }
  .cover-portrait {
    position: absolute; left: 40px; top: 40px; width: 380px; height: 330px;
    background: radial-gradient(ellipse at 50% 60%, var(--skin-mid) 0%, var(--skin-dark) 55%, var(--cover-black) 100%);
  }
  .cover-globe {
    position: absolute; left: 40px; top: 300px; width: 380px; height: 380px; border-radius: 50%;
    background: radial-gradient(circle at 40% 35%, #9bbbd8 0%, var(--globe-blue) 45%, var(--globe-deep) 100%);
  }
  .cover-author {
    position: absolute; top: 30px; width: 100%; text-align: center;
    font-family: "Questrial", sans-serif; color: var(--title-white);
    font-size: 15px; letter-spacing: 9px;
  }
  .cover-title {
    position: absolute; left: 0; width: 100%; top: 442px; text-align: center;
    font-family: "Questrial", sans-serif; line-height: 1;
  }
  .cover-title .title-main { font-size: 86px; color: var(--title-white); letter-spacing: -1px; }
  .cover-title .title-main .initial { color: var(--title-red); font-size: 104px; }
  .cover-title .title-main .the { color: var(--title-white); font-size: 30px; vertical-align: 46px; margin-right: -30px; position: relative; }
  .cover-title .title-sub { font-size: 40px; color: var(--title-white); margin-top: 4px; }

  /* Postcard */
  .postcard {
    position: absolute; left: 550px; top: 194px; width: 613px; height: 459px;
    background: var(--card-white); display: flex;
    box-shadow: 0 5px 14px rgba(0,0,0,.3);
  }
  .postcard-message {
    position: relative; width: 319px; height: 100%; padding: 24px 20px 0;
    background: linear-gradient(180deg, var(--panel-light) 0%, var(--panel-mid) 100%);
  }
  .message-backdrop {
    position: absolute; left: 40px; top: 80px; width: 240px; height: 300px;
    background: radial-gradient(ellipse at 50% 40%, rgba(255,255,255,.7) 0%, rgba(255,255,255,0) 70%);
  }
  .message-content { position: relative; }
  .card-author {
    text-align: center; font-family: "Questrial", sans-serif;
    font-size: 15px; letter-spacing: 5px; color: var(--ink);
  }
  .card-title {
    text-align: center; margin-top: 10px; color: var(--ink);
    font-family: "Questrial", sans-serif; line-height: 1;
  }
  .card-title .title-main { font-size: 42px; letter-spacing: -1px; }
  .card-title .title-main .the { font-size: 11px; vertical-align: 24px; margin-right: -14px; position: relative; }
  .card-title .title-sub { font-family: "Open Sans", sans-serif; font-weight: 700; font-size: 15px; margin-top: 2px; }
  .lead {
    margin-top: 22px; color: var(--title-red); font-weight: 700;
    font-size: 11.6px; line-height: 1.4;
  }
  .body-copy p {
    margin-top: 8px; font-size: 8.6px; line-height: 1.55; color: var(--body-ink); text-align: justify;
  }

  .postcard-address { position: relative; flex: 1; }
  .stamp-box {
    position: absolute; right: 22px; top: 24px; width: 74px; height: 50px;
    border: 1px solid var(--stamp-line);
  }
  .order-info {
    position: absolute; right: 22px; top: 250px; text-align: right;
    font-family: "EB Garamond", serif; font-size: 10.5px; line-height: 1.4; color: var(--ink);
  }
  .order-info .gap { margin-top: 12px; }
  .publisher {
    position: absolute; right: 22px; bottom: 30px; text-align: center;
    font-family: "EB Garamond", serif; color: var(--ink);
  }
  .publisher .mark { width: 14px; height: 14px; border-radius: 50%; background: var(--ink); margin: 0 auto 4px; }
  .publisher .name { font-size: 17px; font-weight: 600; letter-spacing: .5px; }
  .publisher .division { font-size: 5.5px; letter-spacing: .4px; }
</style>
</head>
<body>

<section class="book-cover" aria-label="Book cover">
  <div class="cover-portrait" role="img" aria-label="Photograph of a hooded man's eyes looking out of the shadow"></div>
  <div class="cover-globe" role="img" aria-label="Photograph of planet Earth rising at the bottom of the cover"></div>
  <p class="cover-author">ELI MARSDEN</p>
  <h1 class="cover-title">
    <div class="title-main"><span class="the">The</span><span class="initial">E</span>NEMY</div>
    <div class="title-sub">in Modern Eden</div>
  </h1>
</section>

<article class="postcard">
  <section class="postcard-message">
    <div class="message-backdrop" role="img" aria-label="Faint image of the book cover behind the text"></div>
    <div class="message-content">
      <p class="card-author">ELI MARSDEN</p>
      <h2 class="card-title">
        <div class="title-main"><span class="the">The</span>ENEMY</div>
        <div class="title-sub">In Modern Eden</div>
      </h2>
      <p class="lead">There is a ferocious enemy in our world that’s wreaking havoc in human culture. His name is Satan (the Devil), but millions of people don’t believe that he exists.</p>
      <div class="body-copy">
        <p>Despite the widespread preaching of the gospel, only 4 in 10 (40%) American Christians believe that Satan exist. Those who believe think of him not as a real being but only as a symbol of evil.</p>
        <p>Satan is not only real but deeply entrenched in modern societies, harming us in ways that we can’t possibly imagine.</p>
        <p>Discover how he influences people daily, regardless of their religious beliefs, for his purpose.</p>
        <p>The Enemy in Modern Eden not only exposes Satan’s diabolical schemes in our world, but also shows how you can defend yourself against the most dangerous and aggressive personality in the universe and make it to heaven safely.</p>
      </div>
    </div>
  </section>

  <section class="postcard-address">
    <div class="stamp-box" aria-label="Stamp area"></div>
    <div class="order-info">
      <p>Available now from Holbar Press</p>
      <p>www.holbarpress.com</p>
      <p class="gap">Order this title through your local bookseller</p>
      <p>or preferred on-line retailer.</p>
      <p>978-0-5512-4410-3 (SC ISBN)</p>
      <p>978-0-5512-4411-0 (HC ISBN)</p>
      <p>978-0-5512-4412-7 (Ebook ISBN)</p>
    </div>
    <div class="publisher">
      <div class="mark"></div>
      <div class="name">HOLBAR PRESS</div>
      <div class="division">A DIVISION OF NORTHGATE &amp; ELM HOUSE</div>
    </div>
  </section>
</article>

</body>
</html>
```